Postcard for Antique Furniture Restorer

My business is to restore antique furniture. I am based in Sydney, Australia.

I will be using this postcard to promote my business.
I will give it to customers like a With Compliments card.

Sometimes I will be writing information on the back of the card.

Design for Postcard Size eg 148 X 105mm

Front of card:

Attached are images of Antique furniture - please use ONLY 1 of the 3 images.
Deep etch the image on a white or cream background.

On front of card add these words:
Timber Reborn
antique furniture restoration

Antiques travel through time, seeing generations of families
Through time they remain - they tell a continuing story
Be part of the journey

Back of postcard:
(leave space for notes to be handwritten)

Add these words:

Timber Reborn
Corin Maddox
mobile 0437 552 618
www.oakandvarnishcraft.com.au

Industry/Entity Type

Business

Font styles to use
Serif
Sans Serif

Colors
fefdec
ffffff

Requirements
Must have
• Use only 1 image. Image must be deep etched.

```html
<!DOCTYPE html>
<html lang="en">
<head>
<meta charset="utf-8">
<title>Timber Reborn — Postcard Front</title>
<link rel="stylesheet" href="https://fonts.googleapis.com/css2?family=Libre+Franklin:wght@500;600;700&display=swap">
<style>
  :root {
    --backdrop: #e4e3e0;
    --card: #ffffff;
    --timber-dark: #4a180b;
    --timber-mid: #7a2c15;
    --timber-light: #a3461f;
    --title-ink: #5a2112;
    --reverse-ink: #ffffff;
  }
  html, body {
    margin: 0;
    width: 1200px;
    height: 798px;
    overflow: hidden;
    background: var(--backdrop);
  }
  .postcard {
    position: absolute;
    left: 40px;
    top: 60px;
    width: 1120px;
    height: 678px;
    background: var(--card);
    overflow: hidden;
    font-family: "Libre Franklin", Arial, sans-serif;
  }
  .timber-etch {
    position: absolute;
    inset: 0;
    width: 100%;
    height: 100%;
  }
  .brand-title {
    position: absolute;
    top: 300px;
    left: 94px;
    margin: 0;
    font-size: 80px;
    font-weight: 600;
    letter-spacing: 6px;
    line-height: 1;
    white-space: nowrap;
  }
  .brand-title .word-light { color: var(--title-ink); }
  .brand-title .word-reverse {
    color: var(--reverse-ink);
    position: absolute;
    left: 448px;
  }
  .tagline {
    position: absolute;
    top: 389px;
    left: 98px;
    margin: 0;
    font-size: 20px;
    font-weight: 700;
    letter-spacing: 1px;
    color: var(--title-ink);
  }
  .story {
    position: absolute;
    right: 120px;
    top: 462px;
    margin: 0;
    text-align: right;
    color: var(--reverse-ink);
    font-size: 17px;
    font-weight: 500;
    letter-spacing: 1.2px;
    line-height: 35px;
  }
</style>
</head>
<body>
  <section class="postcard">
    <svg class="timber-etch" viewBox="0 0 1120 678" role="img" aria-label="Deep-etched slab of rich reddish-brown antique timber with swirling grain">
      <defs>
        <radialGradient id="timberGrain" cx="75%" cy="30%" r="80%">
          <stop offset="0%" stop-color="var(--timber-light)"/>
          <stop offset="45%" stop-color="var(--timber-mid)"/>
          <stop offset="100%" stop-color="var(--timber-dark)"/>
        </radialGradient>
      </defs>
      <path d="M565 0 L1120 0 L1120 678 L254 678 C330 640 400 590 440 520 C480 440 500 340 520 250 C540 150 550 60 565 0 Z" fill="url(#timberGrain)"/>
    </svg>

    <h1 class="brand-title"><span class="word-light">TIMBER</span><span class="word-reverse">REBORN</span></h1>
    <p class="tagline">Antique Furniture Restoration</p>

    <p class="story">
      Antiques travel through time,<br>
      seeing generations of families<br>
      Through time they remain,<br>
      they tell a continuing story<br>
      Be part of the journey
    </p>
  </section>
</body>
</html>
```